Need a logo and business card design for my electrical company.
Company name is Kestrel Volt Electrical
In the bottow right hand corner i need
E.C. 708291 for the momument till i get my contractors license number sent to me.
Design i want black back ground with a picture of Thor's hammer and lighting hitting the top of it.

Industry/Entity Type

Electrical

Contact Information for Business Card

Owner Dermot Ashby Phone number 0412873590 email kestrelvoltelectrical@wirepostmail.com facebook page Kestrel Volt Electrical

```html
<!DOCTYPE html>
<html lang="en">
<head>
<meta charset="utf-8">
<title>Kestrel Volt Electrical – Business Card</title>
<link rel="stylesheet" href="https://fonts.googleapis.com/css2?family=Cinzel:wght@700&family=Roboto+Condensed:wght@400;700&family=Tinos&display=swap">
<style>
  :root {
    --backdrop: #e6c697;
    --card-dark: #2b2b2b;
    --yellow: #f0ee14;
    --amber: #f7b12a;
    --ink: #1f1f1f;
    --white: #ffffff;
  }
  * { margin: 0; padding: 0; box-sizing: border-box; }
  html, body {
    width: 1200px;
    height: 1156px;
    overflow: hidden;
    background: var(--backdrop);
  }
  .card {
    position: absolute;
    left: 60px;
    top: 245px;
    width: 1080px;
    height: 667px;
    background: var(--card-dark);
    overflow: hidden;
    box-shadow: 0 6px 18px rgba(0,0,0,0.35);
  }
  .card-band {
    position: absolute;
    left: 0;
    top: 0;
    width: 1080px;
    height: 667px;
  }
  .brand-badge {
    position: absolute;
    left: 71px;
    top: 53px;
    width: 450px;
    height: 450px;
    border-radius: 50%;
    background: linear-gradient(145deg, var(--yellow) 30%, var(--amber) 100%);
    display: flex;
    align-items: center;
    justify-content: center;
    text-align: center;
  }
  .brand-badge-name {
    font-family: "Roboto Condensed", sans-serif;
    font-weight: 700;
    font-size: 50px;
    line-height: 1.1;
    color: var(--ink);
    width: 320px;
  }
  .company-heading {
    position: absolute;
    right: 104px;
    top: 60px;
    text-align: right;
  }
  .company-name {
    font-family: "Cinzel", serif;
    font-weight: 700;
    font-size: 78px;
    line-height: 1;
    letter-spacing: 1px;
    background: linear-gradient(90deg, var(--yellow), var(--amber));
    -webkit-background-clip: text;
    background-clip: text;
    color: transparent;
  }
  .company-trade {
    font-family: "Roboto Condensed", sans-serif;
    font-weight: 700;
    font-size: 36px;
    color: var(--white);
    margin-top: 18px;
  }
  .contact-list {
    position: absolute;
    right: 104px;
    top: 300px;
    list-style: none;
  }
  .contact-item {
    display: flex;
    align-items: center;
    justify-content: flex-end;
    height: 52px;
    font-family: "Tinos", serif;
    font-size: 31px;
    color: var(--white);
    white-space: nowrap;
  }
  .contact-item--email {
    font-size: 23px;
  }
  .contact-icon {
    width: 30px;
    height: 34px;
    margin-left: 18px;
    flex: none;
  }
  .licence-number {
    position: absolute;
    right: 120px;
    top: 548px;
    font-family: "Roboto Condensed", sans-serif;
    font-size: 36px;
    letter-spacing: 1px;
    color: var(--ink);
  }
</style>
</head>
<body>
  <section class="card">
    <svg class="card-band" viewBox="0 0 1080 667" aria-hidden="true">
      <defs>
        <linearGradient id="bandGradient" x1="0" y1="1" x2="1" y2="0">
          <stop offset="0" stop-color="#f7b12a"/>
          <stop offset="0.75" stop-color="#f0ee14"/>
        </linearGradient>
      </defs>
      <path d="M0 532 H150 Q290 580 430 532 H1080 V667 H0 Z" fill="url(#bandGradient)"/>
    </svg>

    <div class="brand-badge">
      <span class="brand-badge-name">Kestrel Volt Electrical</span>
    </div>

    <header class="company-heading">
      <h1 class="company-name">KESTREL</h1>
      <p class="company-trade">Volt Electrical</p>
    </header>

    <ul class="contact-list">
      <li class="contact-item">0412 873 590
        <svg class="contact-icon" viewBox="0 0 30 34" aria-hidden="true">
          <rect x="5" y="2" width="20" height="30" rx="3" fill="none" stroke="#fff" stroke-width="2.5"/>
          <line x1="8" y1="26" x2="22" y2="26" stroke="#fff" stroke-width="2"/>
          <circle cx="15" cy="29" r="1.3" fill="#fff"/>
        </svg>
      </li>
      <li class="contact-item contact-item--email">kestrelvoltelectrical@wirepostmail.com
        <svg class="contact-icon" viewBox="0 0 30 34" aria-hidden="true">
          <rect x="1.5" y="8" width="27" height="18" rx="1" fill="none" stroke="#fff" stroke-width="2.5"/>
          <path d="M2 9 L15 19 L28 9 M2 25 L11 16 M28 25 L19 16" fill="none" stroke="#fff" stroke-width="2.2"/>
        </svg>
      </li>
      <li class="contact-item">Address
        <svg class="contact-icon" viewBox="0 0 30 34" aria-hidden="true">
          <path d="M15 33 C7 21 5 17 5 12 A10 10 0 0 1 25 12 C25 17 23 21 15 33 Z" fill="#fff"/>
          <circle cx="15" cy="12" r="4" fill="#2b2b2b"/>
        </svg>
      </li>
    </ul>

    <p class="licence-number">E.C. 708291</p>
  </section>
</body>
</html>
```